Bref créative
Business cards, invoice, letterhead
Stationery for baby immunisation service
Professional
Thandeka Zulani
Dr
42 9th Avenue
Brenthill
Johannesburg
drtzulani@kovahealth.co.za
PR 0738261

```html
<!DOCTYPE html>
<html lang="en">
<head>
<meta charset="utf-8">
<title>Tiny Sprouts business card</title>
<link href="https://fonts.googleapis.com/css2?family=Open+Sans:wght@400;600&display=swap" rel="stylesheet">
<style>
  :root {
    --stage: #ece9e6;
    --card-front: #ffffff;
    --card-back: #8e8279;
    --art-dark: #9a8f87;
    --art-light: #d9d3ce;
    --teal: #1ba39c;
    --band-grey: #6b6b6b;
    --ink: #3c3c3c;
    --ink-soft: #777777;
    --rule: #c9c9c9;
  }
  * { margin: 0; padding: 0; box-sizing: border-box; }
  html, body { width: 1200px; height: 402px; overflow: hidden; }
  body {
    background: var(--stage);
    font-family: "Open Sans", Arial, sans-serif;
    position: relative;
  }
  .card {
    position: absolute;
    top: 58px;
    width: 535px;
    height: 283px;
    overflow: hidden;
    box-shadow: 0 3px 10px rgba(0,0,0,0.18);
  }
  .card--front { left: 53px; background: var(--card-front); }
  .card--back { left: 612px; background: var(--card-back); }

  .brand {
    position: absolute;
    top: 84px; left: 0; width: 100%;
    text-align: center;
  }
  .brand__mark {
    display: inline-block;
    width: 13px; height: 13px;
    border-radius: 50%;
    background: var(--teal);
    vertical-align: middle;
    margin-right: 8px;
  }
  .brand__name {
    font-size: 30px;
    font-weight: 600;
    color: var(--teal);
    vertical-align: middle;
    letter-spacing: -0.5px;
  }
  .brand__tagline {
    margin-top: 0;
    font-size: 10.5px;
    color: var(--ink-soft);
    letter-spacing: 0.3px;
  }

  .address {
    position: absolute;
    top: 176px; right: 397px;
    text-align: right;
    font-style: normal;
    font-size: 11.5px;
    line-height: 16px;
    color: var(--ink);
  }
  .divider {
    position: absolute;
    top: 170px; left: 150px;
    width: 1px; height: 62px;
    background: var(--rule);
  }
  .contacts {
    position: absolute;
    top: 172px; left: 160px;
    list-style: none;
    font-size: 11.5px;
    color: var(--ink);
  }
  .contacts li { display: flex; align-items: center; height: 18px; }
  .contacts svg { width: 12px; height: 12px; margin-right: 6px; fill: var(--teal); }

  .licence-band {
    position: absolute;
    left: 0; bottom: 0;
    width: 100%; height: 33px;
    background: var(--band-grey);
    color: #ffffff;
    font-size: 10.5px;
    line-height: 33px;
    padding-left: 14px;
  }
  .name-band {
    position: absolute;
    right: 0; bottom: 0;
    width: 240px; height: 40px;
    background: var(--teal);
    color: #ffffff;
    font-size: 13px;
    font-weight: 600;
    line-height: 40px;
    text-align: center;
  }

  .back-art {
    position: absolute;
    top: 14px; left: 24px; right: 14px; bottom: 14px;
    border-radius: 6px;
    background: linear-gradient(90deg, var(--art-dark) 0%, var(--art-dark) 35%, var(--art-light) 100%);
  }
</style>
</head>
<body>
  <section class="card card--front">
    <div class="brand">
      <span class="brand__mark"></span><span class="brand__name">Tiny Sprouts</span>
      <p class="brand__tagline">infancy to early childhood</p>
    </div>

    <address class="address">42 9th Avenue<br>Brenthill<br>Johannesburg</address>
    <div class="divider"></div>
    <ul class="contacts">
      <li><svg viewBox="0 0 24 24"><path d="M6.6 10.8a15 15 0 0 0 6.6 6.6l2.2-2.2a1 1 0 0 1 1-.25 11.4 11.4 0 0 0 3.6.57 1 1 0 0 1 1 1V20a1 1 0 0 1-1 1A17 17 0 0 1 3 4a1 1 0 0 1 1-1h3.5a1 1 0 0 1 1 1c0 1.25.2 2.45.57 3.57a1 1 0 0 1-.25 1z"/></svg>+27 11 555 0142</li>
      <li><svg viewBox="0 0 24 24"><rect x="6" y="2" width="12" height="20" rx="2"/><rect x="8" y="5" width="8" height="12" fill="#fff"/></svg>+27 82 555 0917</li>
      <li><svg viewBox="0 0 24 24"><path d="M2 5h20v14H2z"/><path d="M2 5l10 8 10-8" fill="none" stroke="#fff" stroke-width="2"/></svg>drtzulani@kovahealth.co.za</li>
    </ul>

    <div class="licence-band">License No: PR 0738261</div>
    <div class="name-band">Dr. Thandeka Zulani</div>
  </section>

  <section class="card card--back">
    <div class="back-art" role="img" aria-label="Illustration area: a faint mother-and-baby drawing on the left and a larger white line drawing of a mother holding a baby on the right, on a taupe ground"></div>
  </section>
</body>
</html>
```